Financial services firm needs updated web design

Our current website, coinpathwealth.example was created by ourselves using templates provided by our website host, Harborline Webworks. We are looking to get a whole new look and feel to our website that is clean, professional and easy to navigate. The design must be able to be transferred to Harborline Webworks for hosting (FTP??-outside my area of expertise - sorry) and that the information can be updated and changed by ourselves in the future. I have included our updated logo and our business card design.
Updates
Project Deadline Extended
Reason: Went away on vacation for two weeks.
Target Market(s)
Age 50+ individuals looking for investment, retirement and estate planning guidance.
Industry/Entity Type
Financial
Number of Pages Required
1 page
Font styles to use
Other font styles liked:
- Adobe Caslon Pro
Look and feel
Each slider illustrates characteristics of the customer's brand and the style your logo design should communicate.

```html
<!DOCTYPE html>
<html lang="en">
<head>
<meta charset="utf-8">
<title>Coinpath Wealth</title>
<link href="https://fonts.googleapis.com/css2?family=Raleway:ital,wght@0,400;0,600;0,700;1,400;1,700&family=Open+Sans:ital,wght@0,400;0,600;1,400&display=swap" rel="stylesheet">
<style>
:root{
  --green:#82b541;
  --ink:#333;
  --muted:#8a8a8a;
  --rule:#e3e3e3;
  --band:#eeeeee;
  --dark:#2e2e2e;
  --darker:#242424;
  --white:#fff;
}
*{box-sizing:border-box;margin:0;padding:0}
html,body{width:800px;height:1200px;overflow:hidden;background:var(--white)}
body{font-family:"Open Sans",sans-serif;color:var(--ink);font-size:5px;line-height:1.6}
.page{position:absolute;left:150px;top:12px;width:500px;height:1168px;background:var(--white);box-shadow:0 0 4px rgba(0,0,0,.08)}
.sec{position:absolute;left:0;width:500px}
h1,h2,h3,h4{font-family:"Raleway",sans-serif}

/* nav */
.nav{top:0;height:46px;display:flex;align-items:stretch;justify-content:space-between;padding:0 16px 0 22px;border-bottom:1px solid var(--rule)}
.brand{display:flex;align-items:center;gap:4px;font-family:"Raleway",sans-serif;font-weight:600;font-size:9px;color:var(--ink)}
.brand i{width:6px;height:6px;background:var(--green);display:block}
.menu{display:flex;list-style:none}
.menu li{display:flex;align-items:center;padding:0 9px;font-family:"Raleway",sans-serif;font-size:5.5px;font-weight:600;color:#555;letter-spacing:.3px}
.menu li.active{background:var(--green);color:var(--white)}

/* hero */
.hero{top:46px;height:178px;background:linear-gradient(135deg,#6d6a66 0%,#8e8a84 40%,#a8a39c 60%,#5f5c58 100%);text-align:center;color:var(--white)}
.hero h1{margin-top:48px;font-size:21px;font-weight:400;letter-spacing:1px;line-height:1.15}
.hero p{margin:8px auto 0;width:300px;font-size:5.5px;color:#f0f0f0}
.arrow{position:absolute;top:80px;width:12px;height:16px;background:rgba(0,0,0,.35);display:flex;align-items:center;justify-content:center}
.arrow.l{left:0}.arrow.r{right:0}

/* specialize */
.intro{top:236px;padding:0 22px}
.intro-head{display:flex;justify-content:space-between;align-items:center}
.intro h2{font-size:8px;font-weight:700;letter-spacing:.3px}
.btn-dark{background:#3a3a3a;color:var(--white);font-family:"Raleway",sans-serif;font-size:5px;font-weight:700;padding:4px 10px;letter-spacing:.4px}
.intro p{margin-top:8px;width:360px;color:var(--muted)}

/* feature columns */
.features{top:328px;padding:0 22px;display:flex;gap:14px}
.feature{flex:1}
.feature .ph{height:80px}
.feature h3{margin-top:8px;font-size:6px;font-weight:700}
.feature h4{font-size:5px;font-weight:400;color:var(--green);font-style:italic}
.feature p{margin-top:5px;color:var(--muted)}

/* quote band */
.quote{top:510px;height:68px;background:var(--band);display:flex;align-items:center;justify-content:center;border-top:1px solid var(--rule);border-bottom:1px solid var(--rule)}
.quote p{font-family:"Raleway",sans-serif;font-size:11px;font-weight:700;font-style:italic;color:#444;letter-spacing:.3px}

/* three info columns */
.info{top:620px;padding:0 22px;display:flex;gap:16px}
.info>div{flex:1}
.info h3{font-size:6px;font-weight:700;margin-bottom:6px}
.acc-item{border:1px solid var(--rule);padding:3px 5px;font-size:5px;margin-bottom:3px;display:flex;align-items:center;gap:4px}
.acc-item b{width:5px;height:5px;background:#bbb;display:block}
.acc-item.open{border-color:var(--green)}
.acc-item.open b{background:var(--green)}
.acc-body{padding:2px 5px 5px;color:var(--muted)}
.bar{margin-bottom:6px}
.bar span{display:block;font-size:4.8px;color:#555}
.bar .track{height:6px;background:#e6e6e6;position:relative}
.bar .fill{position:absolute;left:0;top:0;bottom:0;background:#4a4a4a}
.bar .pct{position:absolute;right:-1px;top:-1px;background:var(--green);color:var(--white);font-size:4px;padding:0 2px;line-height:8px}
.post{display:flex;gap:5px;margin-bottom:7px}
.post .thumb{width:22px;height:18px;flex:none}
.post strong{display:block;font-size:5px;font-weight:600}
.post em{color:var(--muted);font-size:4.5px}

/* testimonial */
.testi{top:790px;text-align:center}
.testi h3{font-size:6px;font-weight:700;letter-spacing:.4px}
.testi h3 span{color:var(--green)}
.avatar{width:22px;height:22px;border-radius:50%;background:#9a9a9a;margin:8px auto}
.testi blockquote{font-family:"Raleway",sans-serif;font-style:italic;font-size:7px;width:300px;margin:0 auto;color:#444}
.testi cite{display:block;margin-top:5px;font-style:normal;font-size:5px;color:var(--muted)}

/* footer */
.footer{top:935px;height:195px;background:var(--dark);color:#aaa;padding:18px 22px;display:flex;gap:12px}
.footer h4{color:var(--white);font-size:5.5px;font-weight:700;margin-bottom:6px;letter-spacing:.3px}
.fcol{flex:1}
.fcol p,.fcol li{font-size:4.8px;list-style:none}
.fcol li{padding:1px 0;border-bottom:1px solid #3c3c3c}
.stats{flex:1.6}
.stat-row{display:flex;gap:18px}
.stat strong{display:block;color:var(--white);font-family:"Raleway",sans-serif;font-size:11px;font-weight:700}
.sub{display:flex;margin-top:10px}
.sub .field{flex:1;height:10px;background:#444}
.sub .go{background:var(--green);color:var(--white);font-size:4.8px;padding:0 6px;line-height:10px}
.social{display:flex;gap:10px;margin-top:14px}
.social div{display:flex;align-items:center;gap:4px;font-size:4.8px}
.social i{width:12px;height:12px;display:block}
.bottom{top:1130px;height:38px;background:var(--darker);display:flex;justify-content:space-between;align-items:center;padding:0 22px;color:#777;font-size:4.8px}
.dots{display:flex;gap:4px}
.dots i{width:5px;height:5px;background:#555;display:block}
</style>
</head>
<body>
<div class="page">

  <header class="sec nav">
    <div class="brand"><i></i>coinpath wealth</div>
    <ul class="menu">
      <li class="active">HOME</li><li>FEATURES</li><li>ABOUT US</li><li>PORTFOLIO</li><li>BLOG</li><li>CONTACT US</li>
    </ul>
  </header>

  <section class="sec hero" role="img" aria-label="Photo of advisors meeting with clients around a table">
    <h1>WELCOME TO COINPATH<br>WEALTH</h1>
    <p>Guidance for investment, retirement and estate planning so you can plan ahead with confidence and enjoy the years that matter most.</p>
    <div class="arrow l"><svg width="5" height="7" viewBox="0 0 5 7"><path d="M4 0L1 3.5 4 7" fill="none" stroke="#fff"/></svg></div>
    <div class="arrow r"><svg width="5" height="7" viewBox="0 0 5 7"><path d="M1 0l3 3.5L1 7" fill="none" stroke="#fff"/></svg></div>
  </section>

  <section class="sec intro">
    <div class="intro-head">
      <h2>WE SPECIALIZE IN ROBUST FINANCIAL SOLUTIONS</h2>
      <span class="btn-dark">CHECK OUR SERVICES</span>
    </div>
    <p>We help individuals over fifty build lasting plans for investment, retirement income and estate transfer. Our advisors listen first, then shape clear strategies around your goals, your family and your timeline.</p>
  </section>

  <section class="sec features">
    <div class="feature">
      <div class="ph" role="img" aria-label="Photo of a financial document being reviewed" style="background:linear-gradient(135deg,#d8d8d8,#8c8c8c)"></div>
      <h3>WHY CHOOSE US</h3>
      <h4>Built on trust and experience</h4>
      <p>Decades of planning experience, plain advice and a steady hand through every market cycle you face.</p>
    </div>
    <div class="feature">
      <div class="ph" role="img" aria-label="Photo of coins and banknotes" style="background:linear-gradient(135deg,#6a5236,#2c2218)"></div>
      <h3>OUR MISSION</h3>
      <h4>To protect what you earned</h4>
      <p>We help you grow, preserve and pass on wealth with clarity, care and a plan built around you.</p>
    </div>
    <div class="feature">
      <div class="ph" role="img" aria-label="Photo of hands working over a desk with a laptop" style="background:linear-gradient(135deg,#c7a98a,#7a6a5c)"></div>
      <h3>WHAT WE DO</h3>
      <h4>Planning for every stage</h4>
      <p>Investment management, retirement income planning and estate strategies under one roof.</p>
    </div>
  </section>

  <section class="sec quote">
    <p>"EVERYTHING IS DESIGNED, BUT SOME THINGS ARE DESIGNED WELL."</p>
  </section>

  <section class="sec info">
    <div>
      <div class="acc-item open"><b></b>Our Company History</div>
      <div class="acc-body">Founded to give families honest planning advice, we have grown one client relationship at a time.</div>
      <div class="acc-item"><b></b>How we plan</div>
      <div class="acc-item"><b></b>Who we serve</div>
      <div class="acc-item"><b></b>Why work with an advisor</div>
    </div>
    <div>
      <h3>Our Capabilities</h3>
      <div class="bar"><span>Investment Planning</span><div class="track"><div class="fill" style="width:90%"></div><em class="pct">90%</em></div></div>
      <div class="bar"><span>Retirement Income</span><div class="track"><div class="fill" style="width:85%"></div><em class="pct">85%</em></div></div>
      <div class="bar"><span>Estate Planning</span><div class="track"><div class="fill" style="width:80%"></div><em class="pct">80%</em></div></div>
      <div class="bar"><span>Tax Strategy</span><div class="track"><div class="fill" style="width:75%"></div><em class="pct">75%</em></div></div>
    </div>
    <div>
      <h3>Recently Posted</h3>
      <div class="post"><div class="thumb" role="img" aria-label="Blog post photo" style="background:#8d8d8d"></div><div><strong>Five steps before you retire</strong><em>March 12 · 3 comments</em></div></div>
      <div class="post"><div class="thumb" role="img" aria-label="Blog post photo" style="background:#a08868"></div><div><strong>Planning your estate with care</strong><em>March 04 · 2 comments</em></div></div>
      <div class="post"><div class="thumb" role="img" aria-label="Blog post photo" style="background:#6f7a84"></div><div><strong>Market update for savers</strong><em>February 21 · 5 comments</em></div></div>
    </div>
  </section>

  <section class="sec testi">
    <h3>WHAT <span>CLIENTS</span> SAY?</h3>
    <div class="avatar" role="img" aria-label="Client portrait placeholder"></div>
    <blockquote>"Their advice made our retirement plan simple to follow, and we finally feel confident about the years ahead of us."</blockquote>
    <cite>Helen Marsh<br>Retired Teacher</cite>
  </section>

  <footer class="sec footer">
    <div class="fcol">
      <h4>ABOUT US</h4>
      <p>Independent planning for investors over fifty.</p>
      <p style="margin-top:6px">214 Alder Row, Suite 5<br>Brookhaven, OR 97000<br>Phone: (555) 014-2290<br>hello@coinpathwealth.example</p>
    </div>
    <div class="fcol">
      <h4>BE HELPFUL</h4>
      <ul><li>Our Services</li><li>Retirement</li><li>Estate Planning</li><li>Investments</li><li>Insurance</li><li>Contact Us</li></ul>
    </div>
    <div class="fcol">
      <h4>RECENT POSTS</h4>
      <ul><li>Five steps before you retire</li><li>Planning your estate with care</li><li>Market update for savers</li><li>Income for the long run</li></ul>
    </div>
    <div class="stats">
      <div class="stat-row">
        <div class="stat"><strong>23,065,423</strong>Assets advised</div>
        <div class="stat"><strong>26,465</strong>Happy clients</div>
      </div>
      <p style="margin-top:8px">Newsletter: plain updates on planning, markets and retirement.</p>
      <div class="sub"><div class="field"></div><span class="go">SUBSCRIBE</span></div>
      <div class="social">
        <div><i style="background:#3b5a98"></i>Follow us<br>on social</div>
        <div><i style="background:#e27d2b"></i>Read our<br>news feed</div>
      </div>
    </div>
  </footer>

  <div class="sec bottom">
    <span>© Coinpath Wealth. All rights reserved.</span>
    <div class="dots"><i></i><i></i><i></i><i></i><i></i><i></i></div>
  </div>

</div>
</body>
</html>
```